Boat Dealership Needs A Post Boat Show Sale Flyer - 8.5X11

We need an 8.5X11 flyer to hand out at our boat show to promote a sale at our dealership following our boat show.

Annual Post Boat Show Open House

February 25 - March 5
Extended Hours
Friday, February 25 - 9 AM to 6 PM
Saturday, February 26 -9 AM to 6 PM
Sunday, February 27 - 11 AM to 3 PM
Monday, February 28 through Friday, March 4 - 9 AM to 6 PM
Saturday, March 5 - 9 AM to 3 PM
After hours by appointment

Phone - (555) 314-2671
Website – callowayboats.example

Didn't buy at the show? Wondering what to do after the show?
Don't miss your last chance to secure boat show season pricing.
Our three large, indoor showrooms are fully stocked, and our discounted boat show pricing continues.
Extended hours and continued show pricing.
In-stock incentives and special financing.
New pontoons in-stock starting at $25,995 and less than $150 a month with approved credit.
New tritoons in stock starting at $38,995 and less than $250 a month with approved credit.
Side console Ripley Hull fishing boats starting at $17,995 and less than $125 a month with approved credit.
Special pricing on remaining in-stock Corvales.
Save thousands on Tidewell.

Family-owned relaxed atmosphere.
Refreshments provided.
Prefer to shop virtually? Shop 24/7 on our website at callowayboats.example or set up a real-time video call.

Proudly Offering – Calloway, Marlo, Ashdowne, and WaveDrift Pontoons, Corvale, Kelaro, Tidewell, Ripley Hull

We would like our brand logos on the design.

Follow Us On Chatterly, Snapverse, and Vidorama

Colors
FFF300
FFF600
FEFA6F
FFFEC7
FFFEE8
FFC000
F8CF3A
FAE287
FDF2CF
FEFAEE
F0912C
F2A743
F7CA91
FBE8D2
FDF5EE
EE7325
F08F49
F5BC92
FAE3D3
FDF4ED
EB3D1F
EC4F4E
F09395
F8D3D4
FCEDEE

```html
<!DOCTYPE html>
<html lang="en">
<head>
<meta charset="utf-8">
<title>Calloway Boating – Post Boat Show Open House Flyer</title>
<link href="https://fonts.googleapis.com/css2?family=Russo+One&family=Montserrat:wght@400;500;600;700;800&display=swap" rel="stylesheet">
<style>
:root{
  --red:#d3131b;
  --red-deep:#b80f16;
  --black:#0d0d0d;
  --white:#ffffff;
  --ink:#1a1a1a;
  --yellow:#FFC000;
  --orange:#F0912C;
  --navy:#22345e;
  --stage:#eceef1;
  --rule:#d7d7d7;
}
*{box-sizing:border-box;margin:0;padding:0}
html,body{width:691px;height:1200px;overflow:hidden}
body{background:var(--stage);font-family:"Montserrat",Arial,sans-serif;color:var(--ink);position:relative}
.flyer{position:absolute;left:130px;width:430px;height:556px;background:var(--white);overflow:hidden;box-shadow:0 6px 18px rgba(0,0,0,.18)}
.flyer--front{top:29px}
.flyer--back{top:614px}
.abs{position:absolute}
.display{font-family:"Russo One","Arial Black",sans-serif;text-transform:uppercase}

/* brand */
.brand{top:16px;left:0;width:430px;display:flex;justify-content:center;align-items:center;gap:8px}
.brand__dot{width:30px;height:30px;border-radius:50%;background:var(--orange)}
.brand__name{font-family:"Russo One",sans-serif;color:var(--red);font-size:17px;letter-spacing:1.5px;line-height:1}

/* hero */
.hero-photo{top:68px;left:0;width:430px;height:240px;background:linear-gradient(180deg,#dfe9f3 0%,#c9dbea 45%,#8aa6b8 62%,#47606e 78%,#2f4452 100%)}
.title{left:0;width:430px;text-align:center;line-height:1}
.title--annual{top:80px;font-size:40px;color:var(--red)}
.title--post{top:119px;font-size:28px;color:var(--black)}
.title--open{top:145px;font-size:42px;color:var(--red)}

/* schedule */
.schedule{top:327px;left:20px;width:180px}
.schedule__dates{font-family:"Russo One",sans-serif;font-size:11px;color:var(--red)}
.schedule__sub{font-size:10.5px;font-weight:500;margin-top:1px}
.schedule__list{list-style:none;margin-top:11px}
.schedule__row{display:flex;justify-content:space-between;align-items:flex-end;font-size:7.4px;font-weight:500;padding:3px 0 4px;border-bottom:1px solid var(--rule)}
.schedule__row:last-child{border-bottom:none}
.schedule__note{margin-top:4px;border:1px dashed var(--red);text-align:center;font-size:10px;font-weight:500;padding:2px 0}

/* footer */
.footer{left:0;bottom:0;width:430px;height:44px;background:var(--black);display:flex;align-items:center;padding:0 20px;color:var(--white)}
.footer__help{font-size:5.8px;font-weight:600;line-height:1.1}
.footer__help strong{display:block;font-family:"Russo One",sans-serif;font-weight:400;color:var(--red);font-size:11px}
.footer__divider{width:1.5px;height:16px;background:var(--yellow);margin:0 12px}
.footer__contact{display:flex;align-items:flex-start;gap:4px}
.footer__phone{font-size:10.5px;font-weight:600;line-height:1}
.footer__web{font-size:4.8px;margin-top:2px}
.footer__addr{font-size:5px;line-height:1.3}
.footer__social{margin-left:auto;text-align:center}
.footer__social span{display:block;font-size:4.3px;color:var(--yellow);margin-bottom:2px}
.footer__icons{display:flex;gap:2px}
.footer__icons i{width:6px;height:6px;border-radius:50%;background:var(--white);display:block}

/* back page */
.back-head{top:32px;left:20px;width:395px}
.back-head__main{font-size:23px;color:var(--red);line-height:1}
.back-head__sub{font-size:12.8px;font-weight:800;letter-spacing:.4px;margin-top:3px;text-transform:uppercase}
.back-head__rule{height:1px;background:var(--rule);margin:5px 0 5px}
.back-head__note{font-size:7.4px;font-weight:700;text-transform:uppercase}
.showroom-photo{top:107px;left:0;width:430px;height:205px;background:linear-gradient(180deg,#0a0a0a 0%,#1b1512 50%,#261c16 80%,#141010 100%)}
.perks{top:121px;left:22px;width:340px;list-style:none;color:var(--white)}
.perks li{position:relative;padding-left:11px;font-size:6.4px;line-height:1.3;margin-bottom:4px}
.perks li::before{content:"";position:absolute;left:0;top:1px;width:6px;height:6px;border-radius:50%;background:var(--red)}
.perks li::after{content:"";position:absolute;left:1.6px;top:2.3px;width:2.6px;height:1.5px;border-left:1px solid var(--white);border-bottom:1px solid var(--white);transform:rotate(-45deg)}

.badges{top:318px;left:20px;width:193px;height:30px;background:var(--red);border-radius:3px;display:flex;align-items:center;gap:10px;padding:0 8px;color:var(--white)}
.badge{display:flex;align-items:center;gap:4px;font-family:"Russo One",sans-serif;font-size:6.4px;line-height:1}
.badge i{width:10px;height:10px;border-radius:50%;border:1.5px solid var(--yellow);display:block;flex:none}
.speedboat-photo{top:352px;left:20px;width:193px;height:74px;background:linear-gradient(180deg,#dde7ef 0%,#c7d6e2 40%,#9fb2c0 70%,#e9eef2 100%)}
.virtual{top:434px;left:20px;width:200px}
.virtual__q{font-size:9.4px;font-weight:600;text-transform:uppercase;line-height:1}
.virtual__cta{font-family:"Russo One",sans-serif;font-size:9.4px;color:var(--red);text-transform:uppercase;line-height:1.05}
.virtual__web{display:inline-block;background:var(--yellow);font-size:5.8px;font-weight:600;padding:1px 4px;margin-top:1px}
.virtual__call{display:inline-block;border:1px dashed var(--red);font-size:7px;font-weight:500;padding:2px 5px;margin-top:5px;text-transform:uppercase}

.offering{top:338px;left:265px;width:160px;color:var(--white)}
.offering__title{font-size:12px;letter-spacing:.3px}
.offering__rule{height:1px;background:var(--yellow);margin:3px 0 8px}
.offering__list{list-style:none;display:grid;grid-template-columns:1fr 1fr;row-gap:6px}
.offering__list li{position:relative;padding-left:9px;font-size:6.3px;font-weight:500;line-height:1.1}
.offering__list li::before{content:"";position:absolute;left:0;top:0;width:6px;height:6px;border-radius:50%;background:var(--yellow)}
.lifestyle{border-radius:50%;border:2.5px solid var(--yellow)}
.lifestyle--a{top:438px;left:296px;width:60px;height:60px;background:linear-gradient(160deg,#9fb7c9,#5d6f7c)}
.lifestyle--b{top:444px;left:346px;width:50px;height:50px;background:linear-gradient(160deg,#c9c27a,#6f7a43)}
</style>
</head>
<body>

<!-- Front page -->
<section class="flyer flyer--front">
  <div class="abs brand"><span class="brand__dot"></span><span class="brand__name">CALLOWAY BOATING</span></div>

  <div class="abs hero-photo" role="img" aria-label="Photo of friends jumping from a pontoon boat on a lake under a cloudy sky"></div>

  <h1 class="display abs title title--annual">Annual</h1>
  <p class="display abs title title--post">Post Boat Show</p>
  <p class="display abs title title--open">Open House</p>

  <svg class="abs" style="top:282px;left:0" width="430" height="48" viewBox="0 0 430 48">
    <path d="M0 14 C30 8 60 20 95 12 C130 4 160 18 200 14 C240 10 270 2 310 8 C350 14 390 2 430 6 L430 48 L0 48Z" fill="#0d0d0d"/>
    <path d="M0 24 C35 18 70 30 110 22 C150 14 185 28 220 24 C260 20 300 12 340 18 C375 23 405 14 430 16 L430 48 L0 48Z" fill="#ffffff"/>
  </svg>

  <svg class="abs" style="top:300px;left:200px" width="230" height="210" viewBox="0 0 230 210" role="img" aria-label="Photo of a family cruising in a pontoon boat across a lake">
    <defs><linearGradient id="lakeGrad" x1="0" y1="0" x2="0" y2="1"><stop offset="0" stop-color="#bfe6f5"/><stop offset=".45" stop-color="#86bfe0"/><stop offset=".7" stop-color="#3a79aa"/><stop offset="1" stop-color="#1f4f7c"/></linearGradient></defs>
    <polygon points="14,10 22,10 60,210 52,210" fill="#d3131b"/>
    <polygon points="22,8 230,0 230,210 60,210" fill="url(#lakeGrad)"/>
  </svg>

  <div class="abs schedule">
    <p class="schedule__dates">February 25 – March 5</p>
    <p class="schedule__sub">Extended Hours</p>
    <ul class="schedule__list">
      <li class="schedule__row"><span>Friday, February 25</span><span>9 AM to 6 PM</span></li>
      <li class="schedule__row"><span>Saturday, February 26</span><span>9 AM to 6 PM</span></li>
      <li class="schedule__row"><span>Sunday, February 27</span><span>11 AM to 3 PM</span></li>
      <li class="schedule__row"><span>Monday, February 28<br>through Friday, March 4</span><span>9 AM to 6 PM</span></li>
      <li class="schedule__row"><span>Saturday, March 5</span><span>9 AM to 3 PM</span></li>
    </ul>
    <p class="schedule__note">After hours by appointment</p>
  </div>

  <svg class="abs" style="top:490px;left:0" width="430" height="24" viewBox="0 0 430 24">
    <path d="M0 10 C40 4 80 16 120 10 C160 4 200 14 240 8 C280 2 320 14 360 8 C390 4 410 10 430 6 L430 24 L0 24Z" fill="#0d0d0d"/>
  </svg>

  <footer class="abs footer">
    <div class="footer__help">WE ARE HERE TO HELP<strong>CONTACT US</strong></div>
    <span class="footer__divider"></span>
    <div class="footer__contact">
      <svg width="7" height="7" viewBox="0 0 24 24"><path d="M6.6 10.8a15 15 0 0 0 6.6 6.6l2.2-2.2c.3-.3.7-.4 1-.2 1.1.4 2.3.6 3.6.6.6 0 1 .4 1 1V20c0 .6-.4 1-1 1A17 17 0 0 1 3 4c0-.6.4-1 1-1h3.5c.6 0 1 .4 1 1 0 1.3.2 2.5.6 3.6.1.3 0 .7-.2 1z" fill="#d3131b"/></svg>
      <div><p class="footer__phone">(555) 314-2671</p><p class="footer__web">callowayboats.example</p></div>
    </div>
    <span class="footer__divider"></span>
    <div class="footer__contact">
      <svg width="6" height="8" viewBox="0 0 24 32"><path d="M12 0a12 12 0 0 0-12 12c0 9 12 20 12 20s12-11 12-20A12 12 0 0 0 12 0zm0 17a5 5 0 1 1 0-10 5 5 0 0 1 0 10z" fill="#d3131b"/></svg>
      <p class="footer__addr">418 Harbor Bend Rd Lakeport,<br>MI 49000</p>
    </div>
    <div class="footer__social"><span>Follow Us</span><div class="footer__icons"><i></i><i></i><i></i></div></div>
  </footer>
</section>

<!-- Back page -->
<section class="flyer flyer--back">
  <div class="abs back-head">
    <h2 class="display back-head__main">Didn't buy at the show?</h2>
    <p class="back-head__sub">Wondering what to do after the show?</p>
    <div class="back-head__rule"></div>
    <p class="back-head__note">Don't miss your last chance to secure boat show season pricing</p>
  </div>

  <div class="abs showroom-photo" role="img" aria-label="Dimmed photo of boats inside an indoor showroom"></div>

  <ul class="abs perks">
    <li>Our three large, indoor showrooms are fully stocked, and our discounted boat show pricing continues</li>
    <li>Extended hours and continued show pricing</li>
    <li>In-stock incentives and special financing</li>
    <li>New pontoons in-stock starting at $25,995 and less than $150 a month with approved credit</li>
    <li>New tritoons in stock starting at $38,995 and less than $250 a month with approved credit</li>
    <li>Side console Ripley Hull fishing boats starting at $17,995 and less than $125 a month with approved credit</li>
    <li>Special pricing on remaining in-stock Corvales</li>
    <li>Save thousands on Tidewell</li>
  </ul>

  <svg class="abs" style="top:290px;left:0" width="430" height="30" viewBox="0 0 430 30">
    <path d="M0 12 C40 6 80 18 120 12 C160 6 200 16 240 10 C280 4 320 14 360 8 C390 4 410 12 430 8 L430 30 L0 30Z" fill="#ffffff"/>
  </svg>

  <svg class="abs" style="top:296px;left:220px" width="210" height="210" viewBox="0 0 210 210" role="img" aria-label="Photo of a wakeboarder behind a towboat on dark blue water">
    <defs><linearGradient id="wakeGrad" x1="0" y1="0" x2="0" y2="1"><stop offset="0" stop-color="#2d4674"/><stop offset=".6" stop-color="#22345e"/><stop offset="1" stop-color="#17233f"/></linearGradient></defs>
    <polygon points="6,10 12,10 44,210 38,210" fill="#d3131b"/>
    <polygon points="12,8 210,0 210,210 44,210" fill="url(#wakeGrad)"/>
  </svg>

  <div class="abs badges">
    <div class="badge"><i></i><span>FAMILY-OWNED<br>RELAXED<br>ATMOSPHERE</span></div>
    <div class="badge"><i></i><span>REFRESHMENTS<br>PROVIDED</span></div>
  </div>
  <div class="abs speedboat-photo" role="img" aria-label="Photo of a bowrider boat with swimmers at the stern"></div>
  <div class="abs virtual">
    <p class="virtual__q">Prefer to shop virtually?</p>
    <p class="virtual__cta">Shop 24/7 on our website</p>
    <span class="virtual__web">at callowayboats.example</span><br>
    <span class="virtual__call">Or set up a real-time video call</span>
  </div>

  <div class="abs offering">
    <p class="display offering__title">Proudly Offering</p>
    <div class="offering__rule"></div>
    <ul class="offering__list">
      <li>CALLOWAY</li><li>Corvale</li>
      <li>Marlo</li><li>Kelaro</li>
      <li>Ashdowne</li><li>Tidewell</li>
      <li>WaveDrift<br>Pontoons</li><li>Ripley Hull</li>
    </ul>
  </div>
  <div class="abs lifestyle lifestyle--a" role="img" aria-label="Round photo of people boarding a boat at the dock"></div>
  <div class="abs lifestyle lifestyle--b" role="img" aria-label="Round photo of a couple walking outdoors"></div>

  <svg class="abs" style="top:490px;left:0" width="430" height="24" viewBox="0 0 430 24">
    <path d="M0 10 C40 4 80 16 120 10 C160 4 200 14 240 8 C280 2 320 14 360 8 C390 4 410 10 430 6 L430 24 L0 24Z" fill="#0d0d0d"/>
  </svg>

  <footer class="abs footer">
    <div class="footer__help">WE ARE HERE TO HELP<strong>CONTACT US</strong></div>
    <span class="footer__divider"></span>
    <div class="footer__contact">
      <svg width="7" height="7" viewBox="0 0 24 24"><path d="M6.6 10.8a15 15 0 0 0 6.6 6.6l2.2-2.2c.3-.3.7-.4 1-.2 1.1.4 2.3.6 3.6.6.6 0 1 .4 1 1V20c0 .6-.4 1-1 1A17 17 0 0 1 3 4c0-.6.4-1 1-1h3.5c.6 0 1 .4 1 1 0 1.3.2 2.5.6 3.6.1.3 0 .7-.2 1z" fill="#d3131b"/></svg>
      <div><p class="footer__phone">(555) 314-2671</p><p class="footer__web">callowayboats.example</p></div>
    </div>
    <span class="footer__divider"></span>
    <div class="footer__contact">
      <svg width="6" height="8" viewBox="0 0 24 32"><path d="M12 0a12 12 0 0 0-12 12c0 9 12 20 12 20s12-11 12-20A12 12 0 0 0 12 0zm0 17a5 5 0 1 1 0-10 5 5 0 0 1 0 10z" fill="#d3131b"/></svg>
      <p class="footer__addr">418 Harbor Bend Rd Lakeport,<br>MI 49000</p>
    </div>
    <div class="footer__social"><span>Follow Us</span><div class="footer__icons"><i></i><i></i><i></i></div></div>
  </footer>
</section>

</body>
</html>
```